Cover for a book titled Tidewater Academy: Give, Grow, Stay Bright

I want an innovative cover for a book. The title is Tidewater Academy: Give, Grow, Stay Bright. The cover should indicate entry into the Earth environment. It isn't a school for children, so anything with apples or blackboards isn't appropriate. I have a design I put together but it's very ordinary. I'm looking for a better design that will intrigue people. We enter Tidewater Academy as children, grow mentally and spiritually, and graduate at death.

Font styles to use
Serif

Colors

Designer to choose colors to be used in the design.

Requirements
Must have
• The Earth globe or something explicitly Earth. This is an entry onto the Earth plane to learn lessons about life, love other people, and be happy.
Should not have
• Nothing public school oriented like chalkboards, teachers, apples, school buildings, and so on.

```html
<!DOCTYPE html>
<html lang="en">
<head>
<meta charset="utf-8">
<title>Tidewater Academy: Give, Grow, Stay Bright — Book Cover</title>
<link rel="stylesheet" href="https://fonts.googleapis.com/css2?family=Anton&family=Courier+Prime:wght@400;700&display=swap">
<style>
  :root {
    --ink: #000000;
    --sun: #efd92f;
    --paper: #ffffff;
    --crimson: #990d0f;
    --land: #1b7a2c;
    --sea: #00aeef;
  }
  html, body {
    margin: 0;
    padding: 0;
    width: 848px;
    height: 1200px;
    overflow: hidden;
    background: var(--sun);
  }
  .cover {
    position: relative;
    width: 848px;
    height: 1200px;
    overflow: hidden;
    background: var(--sun);
  }
  .cover-field {
    position: absolute;
    left: 0;
    top: 0;
    width: 612px;
    height: 1200px;
    background: var(--ink);
    clip-path: polygon(0 0, 612px 0, 612px 980px, 250px 1200px, 0 1200px);
  }
  .earth-globe {
    position: absolute;
    left: 20px;
    top: 280px;
    width: 560px;
    height: 560px;
    border-radius: 50%;
    background:
      radial-gradient(circle at 38% 52%, var(--land) 0%, var(--land) 30%, transparent 55%),
      radial-gradient(circle at 70% 30%, var(--land) 0%, transparent 28%),
      radial-gradient(circle at 40% 38%, var(--sea) 0%, #0a6fa3 70%, #073d5c 100%);
  }
  .title-block {
    position: absolute;
    left: 0;
    top: 0;
    width: 848px;
    height: 1200px;
    pointer-events: none;
  }
  .title-word {
    font-family: "Anton", "Impact", sans-serif;
    text-transform: uppercase;
  }
  .tagline {
    position: absolute;
    background: var(--paper);
    border: 6px solid var(--ink);
    border-radius: 4px;
    font-family: "Courier Prime", "Courier New", serif;
    font-weight: 400;
    color: var(--ink);
    text-transform: uppercase;
    display: flex;
    align-items: center;
    justify-content: center;
    box-sizing: border-box;
    white-space: nowrap;
  }
  .tagline--give {
    left: 74px; top: 410px;
    width: 204px; height: 92px;
    font-size: 44px; letter-spacing: 8px;
    transform: rotate(-16deg);
  }
  .tagline--grow {
    left: 97px; top: 560px;
    width: 230px; height: 88px;
    font-size: 44px; letter-spacing: 10px;
    transform: rotate(8deg);
  }
  .tagline--bright {
    left: 125px; top: 725px;
    width: 250px; height: 62px;
    font-size: 26px; letter-spacing: 5px;
    transform: rotate(-25deg);
  }
  .byline {
    position: absolute;
    left: 359px;
    width: 472px;
    height: 53px;
    display: flex;
    align-items: center;
    justify-content: space-between;
    padding: 0 8px;
    box-sizing: border-box;
    font-family: "Courier Prime", "Courier New", serif;
    font-weight: 700;
    font-size: 29px;
    color: var(--sun);
    letter-spacing: 5px;
    white-space: nowrap;
  }
  .byline--red { top: 1076px; background: var(--crimson); }
  .byline--black { top: 1129px; background: var(--ink); }
</style>
</head>
<body>
<main class="cover">
  <div class="cover-field">
    <div class="earth-globe" role="img" aria-label="The Earth globe with green continents and blue oceans"></div>
  </div>

  <svg class="title-block" width="848" height="1200" viewBox="0 0 848 1200" aria-label="Tidewater Academy">
    <rect class="title-stripe" x="617" y="0" width="22" height="635" fill="var(--paper)"/>
    <rect class="title-stripe" x="812" y="0" width="36" height="635" fill="var(--paper)" opacity="0.9"/>
    <text class="title-word" transform="translate(622,0) rotate(90)" x="6" y="0"
          font-size="250" textLength="625" lengthAdjust="spacingAndGlyphs" fill="var(--ink)">Tidewater</text>
    <text class="title-word" transform="translate(632,0) rotate(90)" x="645" y="0"
          font-size="128" textLength="375" lengthAdjust="spacingAndGlyphs" fill="var(--ink)">Academy</text>
    <text class="title-word" transform="translate(742,0) rotate(90)" x="645" y="0"
          font-size="116" textLength="375" lengthAdjust="spacingAndGlyphs" fill="var(--crimson)">Academy</text>
  </svg>

  <div class="tagline tagline--give">Give</div>
  <div class="tagline tagline--grow">Grow</div>
  <div class="tagline tagline--bright">Stay Bright</div>

  <div class="byline byline--red"><span>R.DEAN</span><span>FOSTER,</span><span>PHD</span></div>
  <div class="byline byline--black"><span>R.DEAN</span><span>FOSTER,</span><span>PHD</span></div>
</main>
</body>
</html>
```